Flyer-Design für Bio Gemüsebau
Sehr gut und schnell auf unsere Bedürfnisse und konkreten Änderungswünsche eingegangen.
Zielgruppe
Bio-Gemüseanbau: Bei uns gibt es über 45 Gemüsekulturen von Aubergine bis Zwiebeln.
Endverbraucher, Menschen, die sich gerne gesund ernähren und Wert auf Nachhaltigkeit und Regionalität legen.
Wir verkaufen am Straßenstand sowie an Abonnenten.
Wir heißen 'Gemüsehof Kleiner Acker' und haben bereits ein Logo (siehe Anhang)
Aufgabenstellung
Es wäre prima, wenn der Flyer allgemeine Infos (siehe Worddatei) zu dem Gemüseangebot und der Gärtnerei enthält.
Wir werden zudem einige Fotos zur Auswahl beilegen.
Es wäre ganz toll, wenn an prominenter Stelle ein Foto Platz finden würde, an dessen Stelle man bei Bedarf z.B. auf eine Veranstaltung oder eine bestimmte Aktion hinweisen könnte. Also, dass wir bei Bedarf dieses Foto entfernen und diesen Platz für einen aktuellen Hinweis nutzen könnten.
Ansonsten sind wir offen, was das Format des Flyers angeht. Wenn das Design auf einem ökologischen Papier funktionieren könnte, wäre das super, da wir ja ein Biobetrieb sind.
Unser Logo muss auf jeden Fall mit drauf, das ist inzwischen schon etabliert.
Weitere Infos auf unserer Homepage www.gemuesehof-kleineracker-beispiel.de (unter Galerie sind auch weitere Fotos, die verwendet werden könnten)
Vielen Dank.

```html
<!DOCTYPE html>
<html lang="de">
<head>
<meta charset="utf-8">
<title>Flyer Gemüsehof Kleiner Acker – DIN lang quer</title>
<link href="https://fonts.googleapis.com/css2?family=Gochi+Hand&family=Montserrat:wght@400;500;700&display=swap" rel="stylesheet">
<style>
  :root{
    --green:#3aa548;
    --green-dark:#2e8a3a;
    --white:#ffffff;
    --ink:#1d1d1b;
    --band:#dcdcdc;
    --canvas:#ececec;
    --hand:"Gochi Hand", cursive;
    --sans:"Montserrat", Arial, sans-serif;
  }
  *{box-sizing:border-box;margin:0;padding:0}
  html,body{width:1200px;height:985px;overflow:hidden;background:var(--canvas)}
  .board{position:relative;width:1200px;height:985px}
  .flyer{position:absolute;width:550px;height:275px;background:var(--white);overflow:hidden;box-shadow:0 3px 8px rgba(0,0,0,.25);font-family:var(--sans);color:var(--ink)}
  .pos-a{left:25px;top:197px}
  .pos-b{left:625px;top:197px}
  .pos-c{left:25px;top:512px}
  .pos-d{left:625px;top:512px}

  .photo{position:absolute}
  .photo-veg{background:radial-gradient(circle at 30% 35%,#8fb861 0,#5d7f3a 30%,#7a3a3f 55%,#3f4a33 80%)}
  .photo-veg-alt{background:radial-gradient(circle at 55% 70%,#e07a2a 0,#b9551f 18%,#6d2d3a 40%,#4d7a34 70%,#39552b 100%)}
  .photo-allium{background:radial-gradient(circle at 40% 45%,#c9d2c4 0,#a3ae9c 30%,#6e7b66 60%,#4f5a4b 100%)}
  .zucchini{position:absolute;height:22px;border-radius:50%;background:linear-gradient(180deg,#6cae3e 0,#2f6a1f 60%,#1f4a15 100%)}

  .logo-badge{position:absolute;width:92px;height:92px;border-radius:50%;background:var(--white);display:flex;align-items:center;justify-content:center;text-align:center;font-family:var(--hand);font-size:15px;line-height:1.05;color:var(--ink);padding:10px}
  .logo-badge.small{width:72px;height:72px;font-size:12px}

  .front-title{position:absolute;left:14px;bottom:38px;font-family:var(--hand);color:var(--white);font-size:66px;line-height:.9}
  .front-title.two-line{font-size:52px;line-height:.95;bottom:30px}
  .title-rule{position:absolute;height:2px;background:var(--white)}
  .photo-caption{position:absolute;left:28px;bottom:8px;color:var(--white);font-size:7px;font-weight:700;line-height:1.2}
  .photo-caption span{display:block;font-weight:400;font-size:5.5px;opacity:.85}

  .info-strip{position:absolute;left:297px;top:0;width:66px;height:182px;background:var(--green);color:var(--white);text-align:center;padding:8px 4px 0}
  .info-strip .lead{font-size:6px;line-height:1.35}
  .info-strip .label{font-size:7px;font-weight:700;text-decoration:underline;margin-top:4px;line-height:1.2}
  .info-strip .dates{font-family:var(--hand);font-size:14px;line-height:1.2;margin-top:4px;text-align:left;padding-left:4px}
  .info-strip .lead + .dates{margin-top:10px}

  .panel{position:absolute;left:368px;top:0;width:182px;height:275px;background:var(--white)}
  .panel-band{position:absolute;left:0;bottom:0;width:100%;height:76px;background:var(--band)}
  .panel h2{position:absolute;left:14px;top:16px;font-family:var(--hand);font-size:19px;font-weight:400;text-decoration:underline;line-height:1}
  .panel .sub{position:absolute;left:22px;top:38px;font-family:var(--hand);font-size:9px}
  .facts{position:absolute;left:14px;top:56px;width:160px;list-style:none;font-size:7.6px;line-height:1.25}
  .facts li{margin-bottom:8px;padding-left:8px;text-indent:-8px}
  .facts li::before{content:"- "}
  .web{position:absolute;font-size:9px;font-weight:700}
  .panel .web{left:0;width:100%;text-align:center;bottom:12px;color:var(--ink)}

  .intro{position:absolute;left:0;top:0;width:184px;height:275px;background:var(--white);padding:20px 14px;font-family:var(--hand);font-size:21px;line-height:1.37}
  .intro.compact{font-size:15px;line-height:1.25;padding:18px 12px}
  .intro.compact p.body{font-family:var(--sans);font-size:7px;line-height:1.6;color:var(--green);margin-top:12px}
  .green-col{position:absolute;left:184px;top:0;width:182px;height:275px;background:var(--green);color:var(--white);padding:20px 10px}
  .green-col p{font-size:9.5px;line-height:1.4}
  .green-col h2{font-family:var(--hand);font-weight:400;font-size:19px;text-decoration:underline;line-height:1}
  .green-col .sub{font-family:var(--hand);font-size:9px;margin:4px 0 8px 6px}
  .green-col .facts{position:static;width:auto;color:var(--white)}
  .contact{position:absolute;left:366px;top:195px;width:184px;height:80px;background:var(--white);text-align:center;font-size:7.2px;line-height:1.6;padding-top:10px}
  .contact .web{position:static;display:block;color:var(--green-dark);margin-top:8px;font-size:8.5px}
</style>
</head>
<body>
<main class="board">

  <!-- Vorderseite Abokiste -->
  <section class="flyer pos-a" aria-label="Vorderseite Abokiste">
    <div class="photo photo-veg" style="left:0;top:0;width:368px;height:275px" role="img" aria-label="Foto: Gemüse der Abo-Kiste auf Gitterkiste – Kohlrabi, Rote Bete, Zucchini, Tomaten, Paprika, Salat"></div>
    <div class="logo-badge" style="left:26px;top:22px">Gemüsehof Kleiner Acker</div>
    <div class="info-strip">
      <p class="lead">Unsere frischen Produkte gibt's an unserem Straßenstand direkt am Feld</p>
      <p class="label">Öffnungs-<br>zeiten:</p>
      <p class="dates">Fr 10–14<br>Sa 10–12</p>
    </div>
    <h1 class="front-title">Abokiste</h1>
    <div class="title-rule" style="left:14px;bottom:40px;width:280px"></div>
    <p class="photo-caption">Inhalt der Abo-Kiste<span>(Beispiel aus der Saison 2021)</span></p>
    <div class="panel">
      <div class="panel-band"></div>
      <h2>Abholkiste</h2>
      <p class="sub">Kurz &amp; knackig erklärt</p>
      <ul class="facts">
        <li>Jede Woche 8 bis 10 Gemüsesorten + Kräuter</li>
        <li>Abo von Mai bis Dezember</li>
        <li>20€ pro Woche</li>
        <li>Keine chemisch/synthetischen Dünger oder Spritzmittel</li>
        <li>Abholung in Wiesental</li>
      </ul>
      <div class="zucchini" role="img" aria-label="Foto: Zucchini" style="left:28px;top:188px;width:120px"></div>
      <p class="web">gemuesehof-kleineracker-beispiel.de</p>
    </div>
  </section>

  <!-- Vorderseite Workshop -->
  <section class="flyer pos-b" aria-label="Vorderseite Workshop Sorten und Vielfalt">
    <div class="photo photo-allium" style="left:0;top:0;width:368px;height:275px" role="img" aria-label="Foto: blühender Lauch-Samenstand vor Zaun"></div>
    <div class="logo-badge" style="left:26px;top:22px">Gemüsehof Kleiner Acker</div>
    <div class="info-strip" style="height:205px">
      <p class="lead">Anstehende Termine</p>
      <p class="dates">Sa 12.08<br>Sa 20.08<br>Sa 12.09<br>Sa 18.09<br>Sa 31.09</p>
    </div>
    <h1 class="front-title two-line">Sorten &amp;<br>&nbsp;Vielfalt</h1>
    <div class="title-rule" style="left:14px;bottom:86px;width:250px"></div>
    <div class="title-rule" style="left:24px;bottom:30px;width:220px"></div>
    <div class="panel">
      <div class="panel-band"></div>
      <h2>Workshopinhalt</h2>
      <p class="sub">Kurz &amp; knackig erklärt</p>
      <ul class="facts">
        <li>Jede Woche 8 bis 10 Gemüsesorten + Kräuter</li>
        <li>Abo von Mai bis Dezember</li>
        <li>20€ pro Woche</li>
        <li>Keine chemisch/synthetischen Dünger oder Spritzmittel</li>
        <li>Abholung in Wiesental</li>
      </ul>
      <div class="zucchini" role="img" aria-label="Foto: Zucchini" style="left:28px;top:188px;width:120px"></div>
      <p class="web">gemuesehof-kleineracker-beispiel.de</p>
    </div>
  </section>

  <!-- Rückseite Abokiste -->
  <section class="flyer pos-c" aria-label="Rückseite Abokiste">
    <div class="intro">Wir sind eine kleine Viel-faltsgärtnerei in Wiesental, die Gemüse im Einklang mit der Natur pro-duziert.</div>
    <div class="green-col">
      <p>Als Gemüsekisten-Abonnent leistest Du einen wichtigen Beitrag für die regionale Landwirtschaft. Und Du bist sicher, jede Woche frisches Gemüse direkt aus Wiesental zu erhalten und zahlst weniger als beim Kauf am Stand.</p>
      <div class="zucchini" role="img" aria-label="Foto: Zucchini" style="left:28px;top:212px;width:125px"></div>
    </div>
    <div class="photo photo-veg-alt" style="left:366px;top:0;width:184px;height:195px" role="img" aria-label="Foto: Kürbis, Karotten, Salat und Artischocke"></div>
    <div class="logo-badge small" style="left:422px;top:62px">Gemüsehof Kleiner Acker</div>
    <div class="contact">
      Lena Beispiel, <b>0151 0000 4821</b><br>Feldweg 7, 12345 Wiesental<br>info@gemuesehof-kleineracker-beispiel.de
      <span class="web">gemuesehof-kleineracker-beispiel.de</span>
    </div>
  </section>

  <!-- Rückseite Workshop -->
  <section class="flyer pos-d" aria-label="Rückseite Workshop">
    <div class="intro compact">Wir sind eine kleine Vielfaltsgärtnerei in Wiesental, die Gemüse im Einklang mit der Natur pro-duziert.
      <p class="body">Als Gemüsekisten-Abonnent leistest Du einen wichtigen Beitrag für die regionale Landwirtschaft. Und Du bist sicher, jede Woche frisches Gemüse direkt aus Wiesental zu erhalten und zahlst weniger als beim Kauf am Stand.</p>
    </div>
    <div class="green-col">
      <h2>Abholkiste</h2>
      <p class="sub">Kurz &amp; knackig erklärt</p>
      <ul class="facts">
        <li>Jede Woche 8 bis 10 Gemüsesorten + Kräuter</li>
        <li>Abo von Mai bis Dezember</li>
        <li>20€ pro Woche</li>
        <li>Keine chemisch/synthetischen Dünger oder Spritzmittel</li>
        <li>Abholung in Wiesental</li>
      </ul>
      <div class="zucchini" role="img" aria-label="Foto: Zucchini" style="left:28px;top:212px;width:125px"></div>
    </div>
    <div class="photo photo-veg-alt" style="left:366px;top:0;width:184px;height:195px" role="img" aria-label="Foto: Kürbis, Karotten, Salat und Artischocke"></div>
    <div class="logo-badge small" style="left:422px;top:62px">Gemüsehof Kleiner Acker</div>
    <div class="contact">
      Lena Beispiel, <b>0151 0000 4821</b><br>Feldweg 7, 12345 Wiesental<br>info@gemuesehof-kleineracker-beispiel.de
      <span class="web">gemuesehof-kleineracker-beispiel.de</span>
    </div>
  </section>

</main>
</body>
</html>
```